Design for Glimmora Ad to promote Laptops purchase

Need a graphic design for a Glimmora Ad - to promote 2 laptops (PC and Vantrel) with the stated required ad-text.

AD TEXT:

FOR SME BUSINESS ONLY!
Chat with us!
To get advice on how to apply
and defray up to 80%* of business laptop purchase cost!

*Terms and Conditions apply

Image for reference only

Target Market(s)

Small medium business

Font styles to use
Sans Serif

Requirements
Must have
• 2 laptop images (see attached ) - 1 vector image of VANTREL , and pls try to create another vector image of PC laptop (where screen is showing Blue Quorvex screen)

```html
<!DOCTYPE html>
<html lang="en">
<head>
<meta charset="utf-8">
<title>Glimmora – SME Business Laptop Ad</title>
<link rel="stylesheet" href="https://fonts.googleapis.com/css2?family=Oswald:wght@700&family=Montserrat:ital,wght@0,600;0,700;1,700&display=swap">
<style>
  :root {
    --blue-deep: #1550c4;
    --blue-mid: #3f7be0;
    --sky-pale: #dfe9f5;
    --paper: #f2f3f5;
    --accent-blue: #2a57e6;
    --edge-blue: #2f66d8;
    --highlight: #45b8f0;
    --terms: #4aa8f0;
    --white: #ffffff;
    --note-grey: #6f747c;
  }
  * { margin: 0; padding: 0; box-sizing: border-box; }
  html, body { width: 1200px; height: 1200px; overflow: hidden; background: var(--paper); }
  .ad {
    position: relative;
    width: 1200px;
    height: 1200px;
    overflow: hidden;
    font-family: "Montserrat", sans-serif;
    background: linear-gradient(180deg, var(--blue-deep) 0%, var(--blue-mid) 22%, var(--sky-pale) 45%, var(--paper) 62%, var(--paper) 100%);
  }
  .wave-field {
    position: absolute;
    inset: 0 0 300px 0;
    background: radial-gradient(ellipse at 85% 35%, rgba(255,255,255,0.45), rgba(255,255,255,0) 55%),
                radial-gradient(ellipse at 15% 20%, rgba(120,180,240,0.35), rgba(120,180,240,0) 50%);
  }
  .headline {
    position: absolute;
    top: 138px;
    left: 0;
    width: 1200px;
    text-align: center;
    font-family: "Oswald", sans-serif;
    font-weight: 700;
    font-size: 106px;
    line-height: 1;
    color: var(--white);
    text-shadow: 4px 6px 8px rgba(10, 30, 80, 0.45);
  }
  .laptop { position: absolute; border-radius: 14px; }
  .laptop--pc {
    left: 58px; top: 386px; width: 640px; height: 334px;
    background: linear-gradient(160deg, #1a4fd0 0%, #1d8bf0 55%, #c9ced6 88%, #e4e6ea 100%);
  }
  .laptop--vantrel {
    left: 506px; top: 412px; width: 682px; height: 352px;
    background: linear-gradient(200deg, #0c0c14 0%, #4a1e63 35%, #b05bb6 60%, #c9ccd2 90%, #e6e7ea 100%);
  }
  .reference-note {
    position: absolute;
    left: 103px; top: 818px;
    font-size: 17px; font-weight: 700;
    letter-spacing: 0.5px;
    color: var(--note-grey);
  }
  .base-band { position: absolute; left: 0; top: 0; width: 1200px; height: 1200px; }
  .cta-pill {
    position: absolute;
    left: 430px; top: 892px;
    width: 370px; height: 78px;
    border-radius: 20px;
    background: var(--accent-blue);
    color: var(--white);
    font-weight: 700;
    font-size: 43px;
    line-height: 78px;
    text-align: center;
  }
  .offer__line {
    position: absolute;
    left: 0;
    width: 1200px;
    text-align: center;
    white-space: nowrap;
    color: var(--white);
    font-weight: 700;
    font-size: 43px;
  }
  .offer__line--first { top: 988px; height: 52px; line-height: 52px; }
  .offer__line--second { top: 1040px; height: 70px; line-height: 70px; }
  .offer__line--third { top: 1100px; height: 46px; line-height: 46px; }
  .offer__figure {
    color: var(--highlight);
    font-size: 82px;
    line-height: 0;
  }
  .offer__star { font-size: 48px; line-height: 0; vertical-align: 24px; }
  .terms {
    position: absolute;
    left: 0; top: 1152px;
    width: 1200px;
    text-align: center;
    font-style: italic;
    font-weight: 700;
    font-size: 20px;
    line-height: 24px;
    letter-spacing: 1.5px;
    color: var(--terms);
  }
</style>
</head>
<body>
  <main class="ad">
    <div class="wave-field" role="img" aria-label="Flowing white wave-line pattern over blue sky gradient"></div>

    <h1 class="headline">FOR SME BUSINESS ONLY!</h1>

    <div class="laptop laptop--pc" role="img" aria-label="Silver PC laptop, open, showing a blue Quorvex desktop screen"></div>
    <div class="laptop laptop--vantrel" role="img" aria-label="Silver Vantrel laptop, open, showing a purple and pink galaxy wallpaper"></div>

    <svg class="base-band" viewBox="0 0 1200 1200" aria-hidden="true">
      <defs>
        <linearGradient id="bandFill" x1="0" y1="1" x2="1" y2="0">
          <stop offset="0" stop-color="#3e4857"/>
          <stop offset="0.45" stop-color="#232b36"/>
          <stop offset="1" stop-color="#161c24"/>
        </linearGradient>
      </defs>
      <polygon points="0,900 1200,750 1200,764 0,914" fill="var(--edge-blue)"/>
      <polygon points="0,912 1200,762 1200,1200 0,1200" fill="url(#bandFill)"/>
    </svg>

    <p class="reference-note">Images for reference only.</p>

    <div class="cta-pill">Chat with us!</div>

    <div class="offer">
      <p class="offer__line offer__line--first">To get advice on how to apply</p>
      <p class="offer__line offer__line--second">and defray up to <span class="offer__figure">80%</span><span class="offer__star">*</span> of business laptop</p>
      <p class="offer__line offer__line--third">purchase cost!</p>
    </div>

    <p class="terms">*Terms and Conditions apply</p>
  </main>
</body>
</html>
```